Calloway needs a modernized design

We would like a modern update (that can be responsive) to our existing website. Attached are the two existing pages we would like new concepts of - our home page and a page about one of our locations.

Calloway is provides executive offices and virtual office services. Startups, law firms, and financial services are our primary clients. We would like a professional, clean design, leaning towards minimalist. We intend to greatly reduce/eliminate the long paragraphs of text.

Industry/Entity Type

Business Service

Number of Pages Required

2 page

Requirements
Must have
• A design that can be responsive
Nice to have
• Large image(s) on home page that rotate.

```html
<!DOCTYPE html>
<html lang="en">
<head>
<meta charset="utf-8">
<title>Calloway Business Centers</title>
<link rel="stylesheet" href="https://fonts.googleapis.com/css2?family=Lato:wght@400;700&family=Montserrat:wght@500;600&display=swap">
<style>
:root{
  --navy:#27325f;
  --navy-deep:#1d2650;
  --ink:#333a4d;
  --muted:#8a8e99;
  --line:#d6d8de;
  --stripe:#e2e3e6;
  --white:#ffffff;
  --footer:#15171c;
  --footer-bar:#0d0e11;
}
*{box-sizing:border-box;margin:0;padding:0}
html,body{width:1200px;height:2326px;overflow:hidden}
body{font-family:"Lato",sans-serif;color:var(--ink);background:var(--white);position:relative}
.abs{position:absolute}
h2.section-title{font-family:"Montserrat",sans-serif;font-weight:600;font-size:22px;letter-spacing:1.5px;color:var(--navy);text-align:center}
.title-row{position:absolute;left:0;width:1200px;display:flex;align-items:center;justify-content:center;gap:40px}
.title-row .rule{height:16px;background:var(--stripe);flex:0 0 318px}

/* top bar */
.topbar{left:0;top:0;width:1200px;height:24px;border-bottom:1px solid #ececec}
.topbar .socials{left:99px;top:3px;display:flex;gap:5px}
.topbar .socials span{width:16px;height:16px;background:#8a8e99;border-radius:2px}
.topbar .phones{right:99px;top:5px;font-size:12px;font-weight:700;color:var(--ink);letter-spacing:.4px}

/* nav */
.nav{left:0;top:24px;width:1200px;height:66px}
.brand{left:99px;top:8px;display:flex;align-items:center;gap:10px}
.brand .mark{width:48px;height:48px;border-radius:50%;background:var(--navy)}
.brand .name{font-family:"Lato",sans-serif;font-weight:700;font-size:20px;color:var(--navy);line-height:1}
.brand .name small{display:block;font-size:10px;letter-spacing:1px;margin-top:2px}
.menu{right:99px;top:24px;display:flex;gap:40px;font-size:12.5px;letter-spacing:.6px;color:var(--ink)}
.menu a{color:inherit;text-decoration:none;padding-bottom:6px}
.menu a.active{border-bottom:2px solid var(--navy);color:var(--navy)}

/* hero */
.hero{left:0;top:90px;width:1200px;height:505px;background:linear-gradient(180deg,#b9c3cf 0%,#9eabb9 45%,#c8ccd2 100%)}
.hero .title{left:0;top:140px;width:1200px;text-align:center;font-family:"Montserrat",sans-serif;font-weight:600;font-size:48px;color:var(--white);letter-spacing:1px}
.hero .lead{left:195px;top:222px;width:810px;text-align:center;color:var(--white);font-size:15px;font-weight:700;line-height:1.55}
.hero .arrow{top:200px}
.hero .tabs{left:0;top:438px;width:1200px;height:67px;background:rgba(38,52,110,.72);display:flex;justify-content:center}
.hero .tabs div{width:170px;display:flex;align-items:center;justify-content:center;text-align:center;color:var(--white);font-size:12.5px;font-weight:700;line-height:1.2;padding:0 10px}
.hero .tabs div.on{background:rgba(30,40,90,.55)}
.hero .tabs div.sel span{border-bottom:1px solid var(--white)}

/* welcome */
.welcome-text{left:99px;top:705px;width:1002px;text-align:center;font-size:12px;line-height:1.6;color:var(--muted)}

/* services */
.services{left:0;top:812px;width:1200px;height:434px;background:linear-gradient(120deg,#d8cbb9,#a89683 60%,#e6e1da)}
.services .panel{left:0;top:0;width:588px;height:434px;background:linear-gradient(135deg,#2b3a78,#3b4a86)}
.services .panel h2{position:absolute;left:99px;top:42px;width:412px;text-align:center;color:var(--white);font-family:"Montserrat",sans-serif;font-weight:500;font-size:22px;letter-spacing:1px}
.services .panel p{position:absolute;left:99px;width:412px;color:var(--white);font-size:12.5px;line-height:1.55}
.btn-outline{position:absolute;border:1px solid var(--white);color:var(--white);font-size:13px;font-weight:700;display:flex;align-items:center;justify-content:center}
.services .card{left:528px;top:47px;width:572px;height:341px;background:var(--white)}
.feature{position:absolute;width:240px}
.feature .head{display:flex;align-items:center;gap:12px}
.feature .icon{width:51px;height:51px;border:2px solid var(--navy);border-radius:50%;display:flex;align-items:center;justify-content:center;flex:none}
.feature h3{font-weight:400;font-size:15.5px;color:var(--navy)}
.feature p{margin-top:8px;font-size:12px;line-height:1.5;color:var(--muted)}

/* value */
.value-tabs{left:357px;top:1339px;width:486px;height:33px;display:flex;border:1px solid var(--navy)}
.value-tabs div{flex:1;display:flex;align-items:center;justify-content:center;font-size:13.5px;font-weight:700;color:var(--navy)}
.value-tabs div.on{background:var(--navy);color:var(--white)}
.value-text{left:115px;width:970px;text-align:center;font-size:12px;line-height:1.6;color:var(--muted)}

/* contact */
.contact{left:0;top:1531px;width:1200px;height:549px;background:linear-gradient(180deg,#f3f3f4,#e9eaec)}
.contact .person{left:783px;top:127px;width:317px;height:422px;background:linear-gradient(180deg,#dfe2e7,#9aa3b1 60%,#b9c0ca)}
.contact-text{left:99px;top:1613px;width:1002px;text-align:center;font-size:12px;line-height:1.6;color:var(--muted)}
.form{left:99px;top:1692px;width:699px;height:338px;background:var(--white);border:1px solid var(--line)}
.form h3{position:absolute;left:0;top:26px;width:100%;text-align:center;font-family:"Montserrat",sans-serif;font-weight:600;font-size:15px;color:var(--navy);letter-spacing:.5px}
.field{position:absolute;height:31px;border:1px solid #c9ccd3;border-left:4px solid var(--navy);font-size:12px;color:var(--ink);display:flex;align-items:center;padding-left:14px}
.field .caret{position:absolute;right:10px;font-size:8px;color:var(--muted)}
.submit{position:absolute;left:290px;top:276px;width:119px;height:32px;border:1px solid var(--navy);color:var(--navy);font-size:13px;font-weight:700;display:flex;align-items:center;justify-content:center}

/* footer */
.footer{left:0;top:2080px;width:1200px;height:208px;background:linear-gradient(180deg,#1e2026,var(--footer))}
.footer .badge{left:99px;top:31px;width:84px;height:78px;border-radius:50%;background:#6b6f7a}
.footer .about{left:99px;top:114px;width:380px;font-size:11.5px;line-height:1.55;color:#8c8f98}
.footer .social{left:99px;top:163px;display:flex;gap:10px}
.footer .social span{width:28px;height:28px;background:#4a78c8;border-radius:2px}
.footer h4{position:absolute;font-size:13px;font-weight:700;color:var(--white)}
.footer .special{left:485px;top:64px;width:233px;height:127px;background:linear-gradient(135deg,#e9e3d8,#c6b79e 60%,#f1ede6)}
.footer .nav-dot{width:20px;height:20px;border-radius:50%;background:#2a2c33;display:flex;align-items:center;justify-content:center}
.footer .contact-info{left:786px;top:64px;font-size:11px;line-height:1.55;color:#7b7e87}
.footer .map{left:945px;top:67px;width:163px;height:116px;background:radial-gradient(ellipse at center,#5a5d66,#2a2c32 70%);border-radius:40% 30% 45% 35%}
.bottombar{left:0;top:2288px;width:1200px;height:38px;background:var(--footer-bar)}
.bottombar .links{left:99px;top:13px;font-size:10.5px;color:#8c8f98;word-spacing:2px}
.bottombar .copy{right:99px;top:13px;font-size:10.5px;color:#8c8f98}
</style>
</head>
<body>

<header class="topbar abs">
  <div class="socials abs"><span></span><span></span><span></span><span></span></div>
  <div class="phones abs">CALL US 555-010-2300 &nbsp;|&nbsp; HOUSTON 555-014-4500</div>
</header>

<nav class="nav abs">
  <div class="brand abs"><span class="mark"></span><span class="name">CALLOWAY<small>BUSINESS CENTERS</small></span></div>
  <div class="menu abs">
    <a class="active">HOME</a><a>PROPERTIES</a><a>VIRTUAL TOUR &amp; VIDEOS</a><a>PHOTOS</a><a>BROKER REFERRALS</a>
  </div>
</nav>

<section class="hero abs" role="img" aria-label="Photo of smiling business colleagues meeting around a table">
  <h1 class="title abs">LOREM IPSUM IS DUMMY</h1>
  <p class="lead abs">Lorem ipsum dolor sit amet, consectetuer adipiscing elit, sed diam nonummy nibh euismod tincidunt ut laoreet dolore magna aliquam erat volutpat. Ut wisi enim ad minim veniam, quis nostrud exerci tation ullamcorper.</p>
  <svg class="arrow abs" style="left:88px" width="16" height="28" viewBox="0 0 16 28"><polyline points="13,2 3,14 13,26" fill="none" stroke="#fff" stroke-width="2.5"/></svg>
  <svg class="arrow abs" style="left:1097px" width="16" height="28" viewBox="0 0 16 28"><polyline points="3,2 13,14 3,26" fill="none" stroke="#fff" stroke-width="2.5"/></svg>
  <div class="tabs abs">
    <div>Executive office Suites</div>
    <div class="on">On-Demand Meeting Rooms</div>
    <div>On-Demand Traning Rooms</div>
    <div class="sel"><span>Virtual office solutions</span></div>
    <div>Video conference solutions</div>
  </div>
</section>

<div class="title-row" style="top:650px"><span class="rule"></span><h2 class="section-title">WELCOME</h2><span class="rule"></span></div>
<p class="welcome-text abs">Lorem ipsum dolor sit amet, consectetuer adipiscing elit, sed diam nonummy nibh euismod tincidunt ut laoreet dolore Lorem ipsum dolor sit amet, consectetuer adipiscing elit, sed diam nonummy nibh euismod tincidunt ut laoreet dolore magna aliquam erat volutpat. Ut wisi enim ad minim veniam, quis nostrud exerci tation ullamcorper.magna aliquam erat volutpat. Ut wisi enim ad minim veniam, quis nostrud exerci tation ullamcorper.</p>

<section class="services abs" role="img" aria-label="Photo of colleagues working over documents at a desk">
  <div class="panel abs">
    <h2>OUR SERVICES</h2>
    <p style="top:90px">Calloway Business Centers positions its management team in every one of its business centers - we operate with an open-door policy as a medium-sized company without all of the corporate bureaucracy and red tape.</p>
    <p style="top:185px">The service we provide in terms of technology is unparalleled in our industry. We outfit each of our locations with 100Mbps of bandwidth! We have the latest systems in place, with all locations offering IP PBX telephone systems, Corvane IP telephones and Follow Me Technology including Voicemail to Email and Faxline, with local technical support.. All of this is in place to ensure you can operate your business with maximum efficiency.</p>
    <div class="btn-outline" style="left:99px;top:353px;width:121px;height:33px">Read more</div>
  </div>
  <div class="card abs">
    <div class="feature" style="left:22px;top:14px">
      <div class="head"><span class="icon"><svg width="26" height="26" viewBox="0 0 26 26"><circle cx="13" cy="13" r="11" fill="var(--navy)"/><path d="M6 9c4 0 5 3 4 6s3 4 5 2M16 4c0 4 4 4 6 5" stroke="#fff" stroke-width="1.6" fill="none"/></svg></span><h3>Lorem ipsum dummy</h3></div>
      <p>Ut wisi enim ad minim veniam, quis nos trud exerci tation ullamcorper.magna ali quam erat volutpat. Ut wisi enim ad minim veniam, quis nostrud exerci tation ullamcorper.</p>
    </div>
    <div class="feature" style="left:315px;top:14px">
      <div class="head"><span class="icon"><svg width="26" height="26" viewBox="0 0 26 26" fill="none" stroke="var(--navy)" stroke-width="1.6"><rect x="4" y="12" width="5" height="10"/><rect x="10.5" y="5" width="5" height="17"/><rect x="17" y="9" width="5" height="13"/><line x1="2" y1="23" x2="24" y2="23"/></svg></span><h3>Lorem ipsum dummy</h3></div>
      <p>Ut wisi enim ad minim veniam, quis nos trud exerci tation ullamcorper.magna ali quam erat volutpat. Ut wisi enim ad minim veniam, quis nostrud exerci tation ullamcorper.</p>
    </div>
    <div class="feature" style="left:22px;top:174px">
      <div class="head"><span class="icon"><svg width="26" height="26" viewBox="0 0 26 26" fill="none" stroke="var(--navy)" stroke-width="1.6"><rect x="7" y="3" width="12" height="20" rx="1"/><line x1="10" y1="8" x2="16" y2="8"/><line x1="10" y1="12" x2="16" y2="12"/><line x1="10" y1="16" x2="14" y2="16"/></svg></span><h3>Lorem ipsum dummy</h3></div>
      <p>Ut wisi enim ad minim veniam, quis nos trud exerci tation ullamcorper.magna ali quam erat volutpat. Ut wisi enim ad minim veniam, quis nostrud exerci tation ullamcorper.</p>
    </div>
    <div class="feature" style="left:315px;top:174px">
      <div class="head"><span class="icon"><svg width="26" height="26" viewBox="0 0 26 26"><circle cx="13" cy="13" r="12" fill="var(--navy)"/><g fill="#fff"><ellipse cx="13" cy="7" rx="3" ry="5"/><ellipse cx="13" cy="19" rx="3" ry="5"/><ellipse cx="7" cy="13" rx="5" ry="3"/><ellipse cx="19" cy="13" rx="5" ry="3"/></g><circle cx="13" cy="13" r="2" fill="var(--navy)"/></svg></span><h3>Lorem ipsum dummy</h3></div>
      <p>Ut wisi enim ad minim veniam, quis nos trud exerci tation ullamcorper.magna ali quam erat volutpat. Ut wisi enim ad minim veniam, quis nostrud exerci tation ullamcorper.</p>
    </div>
  </div>
</section>

<div class="title-row" style="top:1284px"><span class="rule"></span><h2 class="section-title">VALUE &amp; COMMUNITY</h2><span class="rule"></span></div>
<div class="value-tabs abs"><div>Value</div><div class="on">Community</div></div>
<p class="value-text abs" style="top:1410px">Companies that partner with Calloway share more than a prestigious address. They also share ideas and services. Our Executive Office Business Centers are places where savvy, growing companies can network, interact and learn from one another.</p>
<p class="value-text abs" style="top:1461px">We are also a large part of the community within our home state of Texas. We have been a contributing business member for 15 years, and are proud to say we have built a solid reputation as an upstanding member of the Dallas, Ft. Worth and Houston business communities by honoring our commitments.</p>

<section class="contact abs">
  <div class="person abs" role="img" aria-label="Photo of a businessman in a suit looking at a tablet"></div>
</section>
<div class="title-row" style="top:1566px"><span class="rule"></span><h2 class="section-title">CONTACT US</h2><span class="rule"></span></div>
<p class="contact-text abs">Sometimes you want to go where everybody knows your name. And they're always glad you came. Doin' it our way. There's nothing we wont try. Never heard the word impossible. This time there's no stopping us. Well we're movin' on up to the east side. To a deluxe apartment in the sky.</p>

<form class="form abs">
  <h3>REQUEST INFORMATION</h3>
  <div class="field" style="left:18px;top:68px;width:319px">First Name</div>
  <div class="field" style="left:360px;top:68px;width:319px">Last Name</div>
  <div class="field" style="left:18px;top:115px;width:662px">Company Name</div>
  <div class="field" style="left:18px;top:163px;width:319px">Phone Number</div>
  <div class="field" style="left:360px;top:163px;width:319px">Email</div>
  <div class="field" style="left:18px;top:209px;width:319px">Property Interested in<span class="caret">▼</span></div>
  <div class="field" style="left:360px;top:209px;width:319px">Product Interested in<span class="caret">▼</span></div>
  <div class="submit">Submit</div>
</form>

<footer class="footer abs">
  <div class="badge abs"></div>
  <p class="about abs">Turpis id consectetur. Phasellus maximus dui at neque faliss, ut porttitor sapien semper</p>
  <div class="social abs"><span></span><span style="background:#c9302c"></span><span style="background:#3b5a9a"></span><span style="background:#2a76b0"></span></div>
  <h4 style="left:530px;top:30px">View Current Specials</h4>
  <div class="special abs" role="img" aria-label="Photo of an elegant furnished lounge">
    <div class="nav-dot abs" style="left:-8px;top:53px"><svg width="8" height="8" viewBox="0 0 8 8"><polyline points="6,1 2,4 6,7" fill="none" stroke="#fff" stroke-width="1.5"/></svg></div>
    <div class="nav-dot abs" style="left:221px;top:53px"><svg width="8" height="8" viewBox="0 0 8 8"><polyline points="2,1 6,4 2,7" fill="none" stroke="#fff" stroke-width="1.5"/></svg></div>
  </div>
  <h4 style="left:786px;top:30px">Get In Touch</h4>
  <div class="contact-info abs">Alder Court Road,<br>14/2 Suite, 9th floor<br>Northfield<br><br>+00 (555) 010.220.330<br><br>hello@calloway-offices.test</div>
  <div class="map abs" role="img" aria-label="Map showing the office location"></div>
</footer>

<div class="bottombar abs">
  <div class="links abs">About Us &nbsp;|&nbsp; Contact Us &nbsp;|&nbsp; Forms &nbsp;|&nbsp; Testimonials &nbsp;|&nbsp; FAQs &nbsp;|&nbsp; Careers &nbsp;|&nbsp; Furniture &nbsp;|&nbsp; Specials &nbsp;|&nbsp; Site Map &nbsp;|&nbsp; Privacy</div>
  <div class="copy abs">Copy right © 2016. All Rights Reserved</div>
</div>

</body>
</html>
```